Coralvale Meat Traders Business Cards

We require business cards revamped with our logo. A few details we would like to use.

1. Round Edges
2. Our logo over the top of a wagyu cattle background photo on one side of the card

Other side of the card has the below details.

1. Person Name (First & Last)
2. Job Position
3. Mobile Number
4. Email Address
5. Website Address

Simple & Neat.

Target Market(s)

Sales

Industry/Entity Type

Agriculture

Contact Information for Business Card

CORALVALE MEAT TRADERS

Colors

Designer to choose colors to be used in the design.

Requirements
Must have
• Company Logo

```html
<!DOCTYPE html>
<html lang="en">
<head>
<meta charset="utf-8">
<title>Coralvale Meat Traders – Business Cards</title>
<link rel="stylesheet" href="https://fonts.googleapis.com/css2?family=Libre+Baskerville:wght@700&family=Quicksand:wght@500&display=swap">
<style>
  :root {
    --maroon: #74162a;
    --maroon-soft: rgba(116, 22, 42, 0.08);
    --ink: #3a3a3a;
    --card: #ffffff;
    --card-shade: #eeeeee;
    --page: #d9d9d9;
    --sky: #c9d6de;
    --trees: #5f8f45;
    --lake: #7f94a8;
    --grass: #6aa33c;
  }
  * { box-sizing: border-box; margin: 0; padding: 0; }
  html, body { width: 1200px; height: 900px; overflow: hidden; }
  body {
    background: var(--page);
    display: flex;
    flex-direction: column;
    align-items: center;
    justify-content: center;
    gap: 40px;
    font-family: "Quicksand", sans-serif;
  }
  .card {
    position: relative;
    width: 600px;
    height: 343px;
    border-radius: 28px;
    overflow: hidden;
    box-shadow: 0 8px 22px rgba(0,0,0,0.18);
  }
  /* Front */
  .card-front .scene-photo {
    position: absolute; inset: 0;
    background: linear-gradient(180deg,
      var(--sky) 0%, var(--trees) 24%, #7ea25a 38%,
      var(--lake) 44%, var(--lake) 62%, var(--grass) 76%, #4f7d2c 100%);
  }
  .wordmark {
    position: absolute;
    display: flex;
    align-items: center;
    gap: 10px;
    font-family: "Libre Baskerville", serif;
    font-weight: 700;
    color: var(--maroon);
    letter-spacing: 0.5px;
    line-height: 1;
    white-space: nowrap;
  }
  .wordmark .mark-dot {
    width: 30px; height: 30px; border-radius: 50%;
    background: var(--maroon);
    flex: none;
  }
  .card-front .wordmark { left: 40px; top: 110px; font-size: 24px; }
  /* Back */
  .card-back {
    background: linear-gradient(100deg, var(--card) 0%, var(--card) 55%, var(--card-shade) 100%);
  }
  .card-back .wordmark { left: 34px; top: 118px; font-size: 24px; }
  .faint-circle {
    position: absolute;
    right: -30px; top: 110px;
    width: 240px; height: 240px;
    border-radius: 50%;
    background: var(--maroon-soft);
  }
  .accent-bar {
    position: absolute;
    right: 0; top: 28px;
    width: 18px; height: 48px;
    background: var(--maroon);
  }
  .person {
    position: absolute;
    right: 36px; top: 30px;
    text-align: right;
  }
  .person-name {
    font-family: "Libre Baskerville", serif;
    font-weight: 700;
    font-size: 19px;
    color: var(--maroon);
  }
  .person-role {
    font-size: 17px;
    color: var(--ink);
    margin-top: 4px;
  }
  .contact-list {
    position: absolute;
    left: 36px; bottom: 30px;
    list-style: none;
    display: flex; flex-direction: column; gap: 9px;
  }
  .contact-list li {
    display: flex; align-items: center; gap: 10px;
    font-size: 16px;
    color: var(--ink);
  }
  .contact-list svg { width: 16px; height: 16px; flex: none; }
</style>
</head>
<body>
  <section class="card card-front">
    <div class="scene-photo" role="img" aria-label="Photo of long-haired cattle grazing on green grass beside a lake with trees behind"></div>
    <div class="wordmark"><span class="mark-dot"></span>CORALVALE MEAT TRADERS</div>
  </section>

  <section class="card card-back">
    <div class="faint-circle"></div>
    <div class="accent-bar"></div>
    <div class="person">
      <p class="person-name">DANIEL HARLOW</p>
      <p class="person-role">Director</p>
    </div>
    <div class="wordmark"><span class="mark-dot"></span>CORALVALE MEAT TRADERS</div>
    <ul class="contact-list">
      <li>
        <svg viewBox="0 0 16 16" aria-hidden="true"><rect x="4" y="1" width="8" height="14" rx="1.5" fill="none" stroke="var(--maroon)" stroke-width="1.5"/><line x1="7" y1="12.5" x2="9" y2="12.5" stroke="var(--maroon)" stroke-width="1.2"/></svg>
        415-308-7724
      </li>
      <li>
        <svg viewBox="0 0 16 16" aria-hidden="true"><rect x="1" y="3" width="14" height="10" fill="var(--maroon)"/><polyline points="1,3 8,9 15,3" fill="none" stroke="#fff" stroke-width="1.2"/></svg>
        info@coralvalemeattraders.com
      </li>
      <li>
        <svg viewBox="0 0 16 16" aria-hidden="true"><g fill="none" stroke="var(--maroon)" stroke-width="1.1"><circle cx="8" cy="8" r="6.5"/><ellipse cx="8" cy="8" rx="3" ry="6.5"/><line x1="1.5" y1="8" x2="14.5" y2="8"/><line x1="2.5" y1="4.5" x2="13.5" y2="4.5"/><line x1="2.5" y1="11.5" x2="13.5" y2="11.5"/></g></svg>
        www.coralvalemeattraders.com
      </li>
    </ul>
  </section>
</body>
</html>
```